Infografik im Bereich Artikelbeschreibung für Onlineshop
Zielgruppe
Vertrieb von Saunaaustattung
Aufgabenstellung
Wird als Ergänzung für die Artikelbeschreibung im Webshop benötigt.
Ein Beispiel wo die Infografik platziert werden soll:
https://www.wolkenkessel-shop.de/Bilder/beispiel.jpg
Bildgröße ca. 1200 x 800 px
Als Hintergrund eventuell möglich teilweise oder ganz die Grafik mit den blauen Wassertropfen verwendbar?

```html
<!DOCTYPE html>
<html lang="de">
<head>
<meta charset="utf-8">
<title>Dampfgenerator – Ausstattungsmerkmale</title>
<link rel="stylesheet" href="https://fonts.googleapis.com/css2?family=Roboto+Condensed:wght@700&display=swap">
<style>
  :root{
    --brand:#1b63b4;
    --brand-dark:#14509a;
    --ring:#1a6ec2;
    --pill:#ffffff;
    --line:#ffffff;
    --sky-top:#7fb6da;
    --sky-mid:#4f97c9;
    --sky-deep:#2d74ab;
    --steel-a:#e9ecef;
    --steel-b:#a9b0b7;
  }
  *{margin:0;padding:0;box-sizing:border-box}
  html,body{width:1200px;height:800px;overflow:hidden;background:#fff}
  .infographic{position:relative;width:1200px;height:800px;overflow:hidden;font-family:"Roboto Condensed",Arial Narrow,sans-serif;color:var(--brand)}
  .backdrop{position:absolute;inset:0;background:
      radial-gradient(ellipse 60% 45% at 50% 35%,rgba(255,255,255,.35),transparent 70%),
      linear-gradient(180deg,var(--sky-top) 0%,var(--sky-mid) 45%,var(--sky-deep) 100%)}
  .connectors{position:absolute;inset:0}
  .hub{position:absolute;left:388px;top:189px;width:424px;height:424px;border-radius:50%;border:13px solid var(--ring);background:#fff;overflow:hidden}
  .hub .product{position:absolute;left:58px;top:58px;width:284px;height:284px;border-radius:6px;
      background:linear-gradient(135deg,var(--steel-a) 0%,#cfd4d9 45%,var(--steel-b) 100%)}
  .pill{position:absolute;height:90px;background:var(--pill);display:flex;align-items:center;
      font-size:22px;line-height:27px;text-transform:uppercase;letter-spacing:.2px}
  .pill--left{left:0;width:330px;border-radius:0 45px 45px 0;padding-left:33px}
  .pill--right{left:857px;width:343px;border-radius:45px 0 0 45px;padding-left:115px}
  .pill--tall{height:112px;border-radius:56px 0 0 56px}
  .pill .icon{position:absolute;right:22px;top:15px;width:60px;height:60px}
  .pill .thumb{position:absolute;left:12px;top:15px;width:78px;height:60px;border-radius:8px;
      background:linear-gradient(135deg,#e4e6e8,#8d949b)}
  .tab{position:absolute;width:110px;background:var(--pill);text-align:center;text-transform:uppercase;font-size:10.5px;line-height:13px}
  .tab--top{top:0;height:136px;border-radius:0 0 55px 55px;padding-top:20px}
  .tab--bottom{top:650px;height:150px;border-radius:55px 55px 0 0;padding-top:108px;font-size:9.5px;line-height:12px}
  .tab svg{display:block;margin:0 auto}
  .tab--top svg{margin-top:14px}
  .tab--bottom svg{position:absolute;left:25px;top:18px}
</style>
</head>
<body>
<div class="infographic">
  <div class="backdrop" role="img" aria-label="Hintergrund: beschlagene Glasscheibe mit blauen Wassertropfen"></div>

  <svg class="connectors" width="1200" height="800" aria-hidden="true">
    <g stroke="var(--line)" stroke-width="4">
      <line x1="300" y1="170" x2="600" y2="400"/>
      <line x1="320" y1="285" x2="600" y2="400"/>
      <line x1="320" y1="400" x2="600" y2="400"/>
      <line x1="320" y1="515" x2="600" y2="400"/>
      <line x1="300" y1="630" x2="600" y2="400"/>
      <line x1="890" y1="165" x2="600" y2="400"/>
      <line x1="880" y1="285" x2="600" y2="400"/>
      <line x1="880" y1="400" x2="600" y2="400"/>
      <line x1="880" y1="515" x2="600" y2="400"/>
      <line x1="890" y1="630" x2="600" y2="400"/>
    </g>
  </svg>

  <div class="hub">
    <div class="product" role="img" aria-label="Produktfoto: Nebelstahl Dampfgenerator im Edelstahlgehäuse mit Anschlüssen"></div>
  </div>

  <!-- linke Merkmale -->
  <div class="pill pill--left" style="top:114px">Inkludierte<br>Armoaauslassdüse
    <svg class="icon" viewBox="0 0 60 60"><circle cx="30" cy="26" r="15" fill="var(--brand)"/><rect x="25" y="16" width="10" height="5" fill="#fff"/><circle cx="33" cy="8" r="3" fill="var(--brand)"/><g stroke="var(--brand)" stroke-width="2"><line x1="14" y1="46" x2="10" y2="52"/><line x1="23" y1="48" x2="21" y2="56"/><line x1="37" y1="48" x2="39" y2="56"/><line x1="46" y1="46" x2="50" y2="52"/></g></svg>
  </div>
  <div class="pill pill--left" style="top:231px">Kurze Aufheizzeit
    <svg class="icon" viewBox="0 0 60 60"><path d="M12 18 A24 24 0 1 1 8 34" fill="none" stroke="var(--brand)" stroke-width="2.5"/><path d="M6 14 L13 19 L6 24" fill="none" stroke="var(--brand)" stroke-width="2.5"/><text x="31" y="29" text-anchor="middle" font-size="11" font-family="Roboto Condensed,sans-serif" fill="var(--brand)">4 - 8</text><text x="31" y="42" text-anchor="middle" font-size="11" font-family="Roboto Condensed,sans-serif" fill="var(--brand)">min</text></svg>
  </div>
  <div class="pill pill--left" style="top:351px;padding-left:22px;font-size:21.5px">Ansteuerung von bis<br>zu zwei Duftstoffen
    <svg class="icon" viewBox="0 0 70 60" style="right:8px;width:70px"><text x="2" y="40" font-size="13" font-family="Roboto Condensed,sans-serif" fill="var(--brand)">A</text><circle cx="26" cy="34" r="10" fill="var(--brand)"/><circle cx="26" cy="20" r="4" fill="var(--brand)"/><circle cx="44" cy="34" r="9" fill="var(--brand)"/><rect x="41" y="20" width="6" height="6" fill="var(--brand)"/><text x="57" y="40" font-size="13" font-family="Roboto Condensed,sans-serif" fill="var(--brand)">B</text></svg>
  </div>
  <div class="pill pill--left" style="top:471px">Optional<br>Steuerung per App
    <svg class="icon" viewBox="0 0 60 60"><rect x="14" y="4" width="26" height="44" rx="4" fill="none" stroke="var(--brand)" stroke-width="3"/><path d="M28 30 v-10 a3 3 0 0 1 6 0 v10 l8 2 a4 4 0 0 1 3 5 l-3 14 h-14 l-6-12 a3 3 0 0 1 5-3z" fill="var(--brand)"/></svg>
  </div>
  <div class="pill pill--left" style="top:593px">Elektronische<br>Entkalkung
    <svg class="icon" viewBox="0 0 60 60"><path d="M18 28 h24 v10 h8 l-20 18 l-20-18 h8z" fill="none" stroke="var(--brand)" stroke-width="2.5"/><g fill="var(--brand)"><circle cx="22" cy="20" r="3"/><circle cx="32" cy="14" r="2.5"/><circle cx="38" cy="22" r="3"/><circle cx="28" cy="38" r="2.5"/><circle cx="34" cy="44" r="2"/></g><g stroke="var(--brand)" stroke-width="1.5"><line x1="30" y1="2" x2="30" y2="10"/><line x1="36" y1="4" x2="36" y2="10"/><line x1="42" y1="6" x2="42" y2="12"/></g></svg>
  </div>

  <!-- rechte Merkmale -->
  <div class="pill pill--right" style="top:110px">Manuelles<br>Entkalken
    <div class="thumb" role="img" aria-label="Foto: Entkalkungsanschluss"></div>
  </div>
  <div class="pill pill--right" style="top:229px">Gehäuse<br>Edelstahl<br>S304</div>
  <div class="pill pill--right" style="top:350px">Hochleistungs-<br>heizstäbe
    <div class="thumb" role="img" aria-label="Foto: Heizstab" style="background:linear-gradient(135deg,#f2f2f2,#b98b62)"></div>
  </div>
  <div class="pill pill--right" style="top:470px">Elektronisches<br>Abflussventil
    <div class="thumb" role="img" aria-label="Foto: Abflussventil"></div>
  </div>
  <div class="pill pill--right pill--tall" style="top:590px">Steuerdisplay<br>fliesenbündig<br>einbaubar</div>

  <!-- obere Reiter -->
  <div class="tab tab--top" style="left:330px">Thermoschutz
    <svg width="46" height="54" viewBox="0 0 46 54"><path d="M23 3 L41 9 V26 C41 39 33 47 23 51 C13 47 5 39 5 26 V9Z" fill="none" stroke="var(--brand)" stroke-width="2.5"/><rect x="20" y="14" width="6" height="20" rx="3" fill="none" stroke="var(--brand)" stroke-width="2"/><circle cx="23" cy="37" r="5" fill="var(--brand)"/></svg>
  </div>
  <div class="tab tab--top" style="left:467px">Automatische<br>Selbstreinigung
    <svg width="50" height="50" viewBox="0 0 50 50"><line x1="42" y1="4" x2="26" y2="22" stroke="var(--brand)" stroke-width="3"/><path d="M26 18 L34 26 L22 44 L6 30Z" fill="var(--brand)"/><circle cx="8" cy="44" r="3" fill="var(--brand)"/><circle cx="16" cy="47" r="2" fill="var(--brand)"/></svg>
  </div>
  <div class="tab tab--top" style="left:610px">Kompakte<br>Größe
    <svg width="60" height="50" viewBox="0 0 60 50"><path d="M8 6 V44 H52" fill="none" stroke="var(--brand)" stroke-width="2"/><path d="M8 6 H52 V44" fill="none" stroke="var(--brand)" stroke-width="1.5" stroke-dasharray="3 3"/><text x="31" y="32" text-anchor="middle" font-size="13" font-family="serif" fill="var(--brand-dark)">cm²</text></svg>
  </div>
  <div class="tab tab--top" style="left:755px">Gerät kocht auf<br>ca. 100 C° hoch
    <svg width="56" height="56" viewBox="0 0 56 56"><circle cx="28" cy="28" r="24" fill="none" stroke="var(--brand)" stroke-width="3"/><circle cx="28" cy="28" r="10" fill="var(--brand)"/><g stroke="var(--brand)" stroke-width="2.5"><line x1="28" y1="12" x2="28" y2="44"/><line x1="12" y1="28" x2="44" y2="28"/><line x1="17" y1="17" x2="39" y2="39"/></g><line x1="11" y1="11" x2="45" y2="45" stroke="#fff" stroke-width="6"/><line x1="11" y1="11" x2="45" y2="45" stroke="var(--brand)" stroke-width="3"/></svg>
  </div>

  <!-- untere Reiter -->
  <div class="tab tab--bottom" style="left:330px">Farblichtsteuerung
    <svg width="60" height="60" viewBox="0 0 60 60"><path d="M30 6 a16 16 0 0 1 9 29 v7 h-18 v-7 a16 16 0 0 1 9-29z" fill="none" stroke="var(--brand)" stroke-width="3"/><line x1="22" y1="48" x2="38" y2="48" stroke="var(--brand)" stroke-width="3"/><line x1="24" y1="54" x2="36" y2="54" stroke="var(--brand)" stroke-width="3"/></svg>
  </div>
  <div class="tab tab--bottom" style="left:467px">Ansteuerung<br>Salzsolevernebler
    <svg width="60" height="70" viewBox="0 0 60 70"><rect x="24" y="14" width="18" height="30" rx="3" transform="rotate(30 33 29)" fill="var(--brand)"/><g fill="var(--brand)"><circle cx="18" cy="48" r="2"/><circle cx="14" cy="56" r="1.8"/><circle cx="20" cy="62" r="1.5"/></g></svg>
  </div>
  <div class="tab tab--bottom" style="left:610px">Verbrühschutz<br>Abfluss
    <svg width="60" height="70" viewBox="0 0 60 70"><rect x="24" y="4" width="12" height="46" rx="6" fill="none" stroke="var(--brand)" stroke-width="3"/><circle cx="30" cy="56" r="10" fill="var(--brand)"/><rect x="28" y="20" width="4" height="32" fill="var(--brand)"/></svg>
  </div>
  <div class="tab tab--bottom" style="left:755px">Integrierte<br>Abluftsteuerung
    <svg width="60" height="60" viewBox="0 0 60 60"><circle cx="30" cy="30" r="26" fill="none" stroke="var(--brand)" stroke-width="2.5"/><circle cx="30" cy="30" r="4" fill="var(--brand)"/><g fill="none" stroke="var(--brand)" stroke-width="2.5"><path d="M30 26 C24 18 26 10 32 10 C38 12 36 20 30 26z"/><path d="M33 32 C42 30 48 36 44 42 C40 46 34 40 33 32z"/><path d="M27 32 C22 40 14 42 12 36 C12 30 20 30 27 32z"/></g></svg>
  </div>
</div>
</body>
</html>
```